Local Roofing/Construction company business needs new biz card design

We need a new business card design, current cards are from the start of this operation and generic at best. We are a local Construction Company (General Contractor) with a majority of our work originating from insurance claims-exterior finish work is the main focus (Roofs-Siding-Gutters etc). Heavily involved with homeowners and the low ball offers they receive from insurance company's after a insurable event takes place. I have attached some of our original logo file(s) below.

```html
<!DOCTYPE html>
<html lang="en">
<head>
<meta charset="utf-8">
<title>Stonebay Construction – Business Card</title>
<link rel="stylesheet" href="https://fonts.googleapis.com/css2?family=Lato:wght@400;700;900&display=swap">
<style>
  :root {
    --bg: #2b2d30;
    --card-dark: #0f1f22;
    --card-light: #ffffff;
    --green: #2fd573;
    --ink: #1a2326;
    --grey: #5c6366;
    --rule-light: #d9d3d8;
  }
  * { box-sizing: border-box; margin: 0; padding: 0; }
  html, body { width: 1200px; height: 952px; overflow: hidden; }
  body {
    background: var(--bg);
    font-family: "Lato", sans-serif;
    display: flex;
    align-items: center;
    justify-content: center;
    gap: 48px;
  }
  .card {
    position: relative;
    width: 520px;
    height: 297px;
    border-radius: 22px;
    overflow: hidden;
  }
  .card--front { background: var(--card-light); color: var(--ink); }
  .card--back { background: var(--card-dark); }

  .edge-rule {
    position: absolute;
    left: 0; right: 0; bottom: 24px;
    height: 6px;
  }
  .edge-rule__accent {
    position: absolute; left: 0; top: 1px;
    width: 46%; height: 3px;
    background: var(--green);
  }
  .edge-rule__tail {
    position: absolute; left: 46%; right: 0; top: 0;
    height: 6px;
    clip-path: polygon(0 0, 100% 0, 100% 100%, 2% 100%);
  }
  .card--front .edge-rule__tail { background: var(--card-dark); }
  .card--back .edge-rule__tail { background: var(--rule-light); }

  .wordmark {
    display: flex; align-items: center; gap: 12px;
    font-weight: 900; letter-spacing: 1px;
  }
  .wordmark__mark { background: var(--green); flex: none; }
  .wordmark__name { line-height: 1; }

  .card--front .wordmark { position: absolute; left: 28px; top: 34px; color: var(--ink); font-size: 24px; }
  .card--front .wordmark__mark { width: 30px; height: 30px; }

  .card--back .wordmark {
    position: absolute; inset: 0 0 30px 0; justify-content: center;
    color: var(--green); font-size: 34px;
  }
  .card--back .wordmark__mark { width: 40px; height: 40px; }

  .person { position: absolute; left: 220px; top: 98px; }
  .person__name { font-size: 20px; font-weight: 400; letter-spacing: 0.5px; }
  .person__name b { color: var(--green); font-weight: 900; }
  .person__role { font-size: 13px; color: var(--grey); margin-top: 2px; }

  .contacts { position: absolute; left: 190px; top: 158px; list-style: none; }
  .contacts li {
    display: flex; align-items: flex-start; gap: 9px;
    font-size: 11.5px; color: var(--grey); line-height: 14px; margin-bottom: 6px;
  }
  .contact-icon {
    flex: none; width: 16px; height: 16px; border-radius: 3px;
    background: var(--ink); display: flex; align-items: center; justify-content: center;
  }
  .contact-icon--pin { background: var(--green); }
  .contact-icon svg { width: 10px; height: 10px; }
</style>
</head>
<body>

  <section class="card card--front" aria-label="Business card front">
    <div class="wordmark">
      <span class="wordmark__mark"></span>
      <span class="wordmark__name">STONEBAY</span>
    </div>

    <div class="person">
      <p class="person__name">DANIEL M. <b>HARLOW</b></p>
      <p class="person__role">General Contractor</p>
    </div>

    <ul class="contacts">
      <li>
        <span class="contact-icon contact-icon--pin">
          <svg viewBox="0 0 10 10"><path d="M5 0.5a3.3 3.3 0 0 0-3.3 3.3C1.7 6.3 5 9.5 5 9.5s3.3-3.2 3.3-5.7A3.3 3.3 0 0 0 5 0.5z" fill="#fff"/><circle cx="5" cy="3.8" r="1.2" fill="#2fd573"/></svg>
        </span>
        <span>1720 Cedar Ridge Road<br>Springfield, IL 62704</span>
      </li>
      <li>
        <span class="contact-icon">
          <svg viewBox="0 0 10 10"><path d="M2.2 0.8l1.5 2-0.9 1.1c0.5 1.1 1.3 1.9 2.3 2.4l1.1-0.9 2 1.5-0.9 1.9C4.3 8.6 1.1 5.3 0.9 1.7z" fill="#fff"/></svg>
        </span>
        <span>+1 555 014 2290</span>
      </li>
      <li>
        <span class="contact-icon">
          <svg viewBox="0 0 10 10"><rect x="0.8" y="2" width="8.4" height="6" fill="none" stroke="#fff" stroke-width="1"/><path d="M0.8 2L5 5.5 9.2 2" fill="none" stroke="#fff" stroke-width="1"/></svg>
        </span>
        <span>office@stonebaybuild.com</span>
      </li>
      <li>
        <span class="contact-icon">
          <svg viewBox="0 0 10 10"><path d="M2 1l6 3.2-2.6 0.8 1.8 3.2-1.2 0.7-1.8-3.2L2.3 7.5z" fill="#fff"/></svg>
        </span>
        <span>www.stonebaybuild.com</span>
      </li>
    </ul>

    <div class="edge-rule"><span class="edge-rule__accent"></span><span class="edge-rule__tail"></span></div>
  </section>

  <section class="card card--back" aria-label="Business card back">
    <div class="wordmark">
      <span class="wordmark__mark"></span>
      <span class="wordmark__name">STONEBAY</span>
    </div>
    <div class="edge-rule"><span class="edge-rule__accent"></span><span class="edge-rule__tail"></span></div>
  </section>

</body>
</html>
```